Packaging Design for Peach Halves in Syrup

Hello Designer,
We have to create a packaging design for a peach halves in syrup product.
The design should be eye-catching, appealing to the target europeen market, and convey the product's quality and freshness.
Peach halves in syrup, packed in glass jars with yellow lids. The jar size is as a picture attached below.
Logo : MOLAN
Label Design: Design a label that prominently features the product name in english and french, "Peach Halves in Syrup," "Pêches en moitiés" and highlights key selling points such as "100% Natural" or "No Added Preservatives."
Visual Elements: Incorporate image or illustration of ripe peaches to emphasize the product's freshness and natural ingredients.
Color Scheme: Use a color scheme that complements the yellow lids, making the product stand out on the shelf. Consider using warm, inviting colors to evoke the feeling of freshness.

Nutritional Information: Include a panel for nutritional information.
ingredients list -Eng : peaches, water, Sugar.
-Fr : pêches, eau, sucre.
Barcode: leave a space for barcode.

Target Market(s)

Europe

Font styles to use
Serif
Decorative
Script

Requirements
Must have
• -Product name : ENG and FR, barcode, nutritional information, ingredients : Eng and French.

```html
<!DOCTYPE html>
<html lang="en">
<head>
<meta charset="utf-8">
<title>Peach Halves in Syrup – Jar Label</title>
<link rel="stylesheet" href="https://fonts.googleapis.com/css2?family=Roboto+Slab:wght@400;500;700;800&display=swap">
<style>
  :root {
    --canvas: #ffffff;
    --label-red: #8f1a1a;
    --sun-yellow: #e9ab16;
    --panel-white: #f4f4f4;
    --ink: #161616;
    --line-white: #f2eeee;
    --peach-1: #f6c64a;
    --peach-2: #e8722f;
  }
  * { margin: 0; padding: 0; box-sizing: border-box; }
  html, body {
    width: 1200px; height: 1200px; overflow: hidden;
    background: var(--canvas);
    font-family: "Roboto Slab", Georgia, serif;
  }
  .label {
    position: absolute; left: 50px; top: 171px;
    width: 1100px; height: 858px;
  }
  .label-art { position: absolute; inset: 0; }
  .brand {
    position: absolute; left: 0; width: 1100px; top: 88px;
    text-align: center; color: #ffffff;
    font-weight: 700; font-size: 48px; letter-spacing: 2px; line-height: 1;
  }
  .name-en {
    position: absolute; left: 173px; width: 659px; top: 306px;
    text-align: center; color: var(--ink);
    font-weight: 800; font-size: 74px; line-height: 1; white-space: nowrap;
  }
  .name-sub {
    position: absolute; left: 173px; width: 659px; top: 398px;
    text-align: center; color: var(--ink);
    font-weight: 500; font-size: 36px; line-height: 1;
  }
  .name-fr {
    position: absolute; left: 173px; width: 659px; top: 492px;
    text-align: center; color: #ffffff;
    font-weight: 700; font-size: 44px; line-height: 1.2; white-space: nowrap;
  }
  .claim {
    position: absolute; left: 633px; width: 180px; top: 790px;
    text-align: center; color: var(--ink);
    font-weight: 700; font-size: 17px; line-height: 1.25;
  }
  .ingredients {
    position: absolute; left: 10px; width: 118px; top: 230px;
    color: var(--ink); font-size: 13px; line-height: 1.35;
  }
  .ingredients h3 {
    font-size: 13px; font-weight: 800; text-transform: uppercase;
    margin-top: 12px; margin-bottom: 2px;
  }
  .ingredients h3:first-child { margin-top: 0; }
  .nutrition {
    position: absolute; left: 894px; width: 192px; top: 210px;
    background: var(--panel-white); color: var(--ink);
    border: 2px solid var(--ink); padding: 8px;
    font-size: 12px; line-height: 1.3;
  }
  .nutrition h3 {
    font-size: 14px; font-weight: 800; border-bottom: 3px solid var(--ink);
    padding-bottom: 4px; margin-bottom: 4px;
  }
  .nutrition .per { font-size: 11px; margin-bottom: 4px; }
  .nutrition table { width: 100%; border-collapse: collapse; }
  .nutrition td { border-top: 1px solid #999; padding: 3px 0; }
  .nutrition td:last-child { text-align: right; font-weight: 700; }
  .nutrition .sub td:first-child { padding-left: 10px; }
  .barcode-space {
    position: absolute; left: 914px; width: 152px; top: 610px; height: 96px;
    background: #ffffff; border: 2px dashed var(--ink);
  }
  .net-weight {
    position: absolute; left: 894px; width: 192px; top: 730px;
    text-align: center; color: var(--ink); font-weight: 700; font-size: 16px;
  }
</style>
</head>
<body>
  <div class="label">
    <svg class="label-art" width="1100" height="858" viewBox="0 0 1100 858" xmlns="http://www.w3.org/2000/svg">
      <defs>
        <linearGradient id="band-shade" x1="0" y1="0" x2="1" y2="0">
          <stop offset="0" stop-color="#8a1616"/>
          <stop offset="0.25" stop-color="#a8352d"/>
          <stop offset="1" stop-color="#861414"/>
        </linearGradient>
        <radialGradient id="peach-tones" cx="0.45" cy="0.4" r="0.7">
          <stop offset="0" stop-color="#e8722f"/>
          <stop offset="0.45" stop-color="#f6c64a"/>
          <stop offset="1" stop-color="#f9e3a6"/>
        </radialGradient>
      </defs>
      <rect x="0" y="0" width="1100" height="858" fill="url(#band-shade)"/>
      <polygon points="0,148 138,172 138,858 0,858" fill="#e9ab16"/>
      <polygon points="880,172 1100,140 1100,858 880,858" fill="#e9ab16"/>
      <path d="M0,140 Q300,175 550,250 Q800,175 1100,132" fill="none" stroke="#f2eeee" stroke-width="4"/>
      <line x1="141" y1="172" x2="141" y2="858" stroke="#f2eeee" stroke-width="4"/>
      <line x1="868" y1="172" x2="868" y2="858" stroke="#f2eeee" stroke-width="4"/>
      <path d="M173,187 Q380,205 550,262 Q720,205 832,187 L832,478 L173,478 Z" fill="#f4f4f4"/>
      <path d="M546,262 Q550,276 542,286 A9,9 0 1 0 558,286 Q550,276 554,262 Z" fill="#8f1a1a"/>
      <rect x="173" y="560" width="659" height="298" fill="#f4f4f4"/>
      <rect x="208" y="568" width="370" height="286" rx="40" fill="url(#peach-tones)"
            role="img" aria-label="Photograph of a ripe peach with a leaf and sliced peach halves"/>
      <circle cx="723" cy="708" r="62" fill="none" stroke="#161616" stroke-width="4"/>
      <circle cx="723" cy="708" r="44" fill="none" stroke="#161616" stroke-width="2.5"/>
    </svg>

    <div class="brand">MOLAN</div>
    <div class="name-en">PEACH HALVES</div>
    <div class="name-sub">in Syrup</div>
    <div class="name-fr">Pêches en moitiés</div>
    <div class="claim">NO ADDED PRESERVATIVES</div>

    <div class="ingredients">
      <h3>Ingredients</h3>
      <p>Peaches, water, sugar.</p>
      <h3>Ingrédients</h3>
      <p>Pêches, eau, sucre.</p>
    </div>

    <div class="nutrition">
      <h3>Nutrition / Nutrition</h3>
      <p class="per">Per 100 g / Pour 100 g</p>
      <table>
        <tr><td>Energy / Énergie</td><td>280 kJ / 66 kcal</td></tr>
        <tr><td>Fat / Graisses</td><td>0 g</td></tr>
        <tr><td>Carbohydrate / Glucides</td><td>16 g</td></tr>
        <tr class="sub"><td>Sugars / Sucres</td><td>15 g</td></tr>
        <tr><td>Protein / Protéines</td><td>0.5 g</td></tr>
        <tr><td>Salt / Sel</td><td>0 g</td></tr>
      </table>
    </div>

    <div class="barcode-space" aria-label="Space reserved for barcode"></div>
    <div class="net-weight">Net wt. 106 g</div>
  </div>
</body>
</html>
```